Paul Sefton Personal Card

I am looking for a personal card that has my contact information on the front and then the url for my website on the back. I am a fan of minimal, modern design, but am very open minded to other styles. Both portrait and landscape designs are acceptable. The only other specification that I have is that some sort of graphic of a raven is present somewhere on the card (my last name 'Sefton' means raven in German).
Contact Information for Business Card
Paul Sefton
608.554.1893
paulwsefton@postvane.net
paulwsefton.com
Colors
Designer to choose colors to be used in the design.
Requirements
Must have
- Raven on some part of the card

```html
<!DOCTYPE html>
<html lang="en">
<head>
<meta charset="utf-8">
<title>Paul Sefton Personal Card</title>
<link rel="stylesheet" href="https://fonts.googleapis.com/css2?family=Montserrat:wght@700&family=Quicksand:wght@400&family=Open+Sans:wght@400&display=swap">
<style>
  :root {
    --backdrop: #e9e4de;
    --card-black: #0c0c0c;
    --card-black-glow: #2a2a2a;
    --raven-tone: #050505;
    --card-white: #ffffff;
    --ink: #1b1b1b;
    --url-ink: #e6e6e6;
    --card-shadow: rgba(0, 0, 0, 0.28);
  }
  * { margin: 0; padding: 0; box-sizing: border-box; }
  html, body {
    width: 1200px;
    height: 1000px;
    overflow: hidden;
    background: var(--backdrop);
  }
  .canvas {
    position: relative;
    width: 1200px;
    height: 1000px;
  }
  .card {
    position: absolute;
    left: 250px;
    width: 700px;
    height: 400px;
    border-radius: 36px;
    box-shadow: 0 14px 30px var(--card-shadow);
    overflow: hidden;
  }
  .card-back {
    top: 60px;
    background: radial-gradient(ellipse at 50% 38%, var(--card-black-glow) 0%, var(--card-black) 62%);
  }
  .raven-mark {
    position: absolute;
    left: 200px;
    top: 70px;
    width: 300px;
    height: 170px;
  }
  .site-url {
    position: absolute;
    left: 0;
    right: 0;
    bottom: 70px;
    text-align: center;
    font-family: "Open Sans", sans-serif;
    font-size: 26px;
    color: var(--url-ink);
    letter-spacing: 0.3px;
  }
  .card-front {
    top: 540px;
    background: var(--card-white);
  }
  .contact-block {
    position: absolute;
    right: 36px;
    top: 150px;
    text-align: right;
    color: var(--ink);
  }
  .holder-name {
    font-family: "Montserrat", sans-serif;
    font-weight: 700;
    font-size: 32px;
    letter-spacing: -0.5px;
    margin-bottom: 14px;
  }
  .contact-line {
    display: flex;
    justify-content: flex-end;
    align-items: center;
    gap: 8px;
    font-family: "Quicksand", sans-serif;
    font-size: 22px;
    line-height: 34px;
  }
  .contact-icon {
    width: 20px;
    height: 20px;
    flex: none;
  }
</style>
</head>
<body>
<main class="canvas">
  <section class="card card-back">
    <svg class="raven-mark" viewBox="0 0 300 170" role="img" aria-label="Raven in flight silhouette, wings spread">
      <ellipse cx="150" cy="85" rx="145" ry="70" fill="var(--raven-tone)" opacity="0.75"/>
    </svg>
    <p class="site-url">paulwsefton.com</p>
  </section>

  <section class="card card-front">
    <div class="contact-block">
      <h1 class="holder-name">Paul Sefton</h1>
      <p class="contact-line">608.554.1893
        <svg class="contact-icon" viewBox="0 0 20 20" aria-hidden="true">
          <circle cx="10" cy="10" r="10" fill="var(--ink)"/>
          <rect x="7" y="4" width="6" height="12" rx="1.2" fill="none" stroke="#fff" stroke-width="1.4"/>
          <line x1="9" y1="13.5" x2="11" y2="13.5" stroke="#fff" stroke-width="1.2"/>
        </svg>
      </p>
      <p class="contact-line">paulwsefton@postvane.net
        <svg class="contact-icon" viewBox="0 0 20 20" aria-hidden="true">
          <circle cx="10" cy="10" r="10" fill="var(--ink)"/>
          <rect x="5" y="6.5" width="10" height="7" fill="none" stroke="#fff" stroke-width="1.3"/>
          <polyline points="5,6.5 10,10.5 15,6.5" fill="none" stroke="#fff" stroke-width="1.3"/>
        </svg>
      </p>
    </div>
  </section>
</main>
</body>
</html>
```